Flyer for photo scanning business

Hello,
I need a flyer created for my business that would be suitable for print, to drop in letterboxes in my local community.

I would like the flyer to convey very simply the services I offer which is scanning negatives, slides and VHS tapes to digital files.
Hopefully it can make it look like an easy process, as people are often daunted by the task of sorting through old photos so they don't always get around to having them scanned.

I have a pinned facebook post that can be used by the designer to reference my services. Pricing does not need to be included on the flyer.
http://facebook.com/lanternloftmedia

Target Market(s)

Parents & Grandparents

Requirements
Must have
• Must make my services look simple! Refer to pinned facebook post for detailed outline of my services.

I would like to flyer to point towards my contact details -
www.lanternloft.com
Miriam 0482 917 356

Colours in line with my logo/brand (uploaded to brief).
Nice to have
• Stock images of 35mm film negatives, 8mm film, VHS tapes, or Velmaprint slides would be worth including. I have also uploaded a mockup of the USB sticks that I provide with digitised images.
Should not have
• no prices needed,

```html
<!DOCTYPE html>
<html lang="en">
<head>
<meta charset="utf-8">
<title>Lanternloft Media – Scanning Flyer</title>
<link rel="stylesheet" href="https://fonts.googleapis.com/css2?family=Questrial&display=swap">
<style>
  :root {
    --sky-top: #3a82c2;
    --sky-mid: #6eb0dc;
    --sky-low: #4a95cd;
    --white: #ffffff;
    --band: rgba(255,255,255,0.88);
    --navy: #0d1b3f;
    --slide-red: #d8352e;
    --slide-blue: #7cc6e6;
    --slide-yellow: #e9d23a;
    --wood: #8a5a3a;
    --wood-light: #b07a52;
    --stick-blue: #5b88b8;
    --stick-white: #f2f4f6;
  }
  html, body {
    margin: 0;
    padding: 0;
    width: 848px;
    height: 1200px;
    overflow: hidden;
  }
  .flyer {
    position: relative;
    width: 848px;
    height: 1200px;
    overflow: hidden;
    background: linear-gradient(180deg, var(--sky-top) 0%, var(--sky-mid) 40%, var(--sky-low) 70%, var(--sky-top) 100%);
    font-family: 'Questrial', 'Century Gothic', sans-serif;
    color: var(--white);
  }
  .brand {
    position: absolute;
    top: 34px;
    left: 0;
    width: 848px;
    display: flex;
    justify-content: center;
    align-items: center;
    gap: 22px;
  }
  .brand-dot {
    width: 78px;
    height: 78px;
    border-radius: 50%;
    background: rgba(255,255,255,0.35);
  }
  .brand-name {
    font-size: 34px;
    letter-spacing: 5px;
    line-height: 1.15;
    color: var(--white);
  }
  .headline-line {
    position: absolute;
    left: 0;
    width: 848px;
    text-align: center;
    line-height: 1;
    white-space: nowrap;
  }
  .line-scan { top: 171px; font-size: 37px; }
  .line-scan .big { font-size: 70px; }
  .line-media { top: 241px; font-size: 37px; }
  .line-digital { top: 268px; font-size: 37px; }
  .line-digital .big { font-size: 92px; }
  .photo-band {
    position: absolute;
    left: 0;
    top: 0;
  }
  .usb-stick {
    position: absolute;
    width: 236px;
    height: 92px;
    border-radius: 16px;
    background: linear-gradient(90deg, var(--stick-white) 0 55%, var(--stick-blue) 55% 100%);
    box-shadow: 0 4px 10px rgba(0,0,0,0.2);
  }
  .usb-left { left: -8px; top: 348px; transform: rotate(-33deg); }
  .usb-right { left: 612px; top: 765px; transform: rotate(22deg);
    background: linear-gradient(90deg, var(--stick-blue) 0 50%, var(--stick-white) 50% 100%); }
  .benefit {
    position: absolute;
    line-height: 1;
    white-space: nowrap;
  }
  .benefit-view { left: 394px; top: 899px; font-size: 42px; }
  .benefit-store { left: 272px; top: 940px; font-size: 42px; }
  .benefit-store .lead { font-size: 50px; }
  .benefit-share { left: 334px; top: 993px; font-size: 34px; }
  .benefit-print { left: 198px; top: 1021px; font-size: 45px; }
  .benefit-print .lead { font-size: 50px; }
  .contact {
    position: absolute;
    left: 178px;
    top: 1097px;
    width: 475px;
    height: 74px;
  }
  .contact-frame { position: absolute; left: 0; top: 0; }
  .contact-row {
    position: absolute;
    left: 78px;
    display: flex;
    align-items: center;
    gap: 9px;
    font-size: 27px;
    line-height: 1;
    white-space: nowrap;
  }
  .contact-phone { top: 5px; }
  .contact-web { top: 41px; }
  .contact-icon { width: 24px; height: 24px; flex: none; }
</style>
</head>
<body>
<main class="flyer">

  <svg class="photo-band" width="848" height="1200" viewBox="0 0 848 1200">
    <defs>
      <clipPath id="photoStrip">
        <polygon points="0,543 848,319 848,737 0,964"/>
      </clipPath>
      <linearGradient id="negativesTone" x1="0" y1="0" x2="1" y2="1">
        <stop offset="0" stop-color="#2a3a66"/>
        <stop offset="1" stop-color="#0a1434"/>
      </linearGradient>
      <linearGradient id="slidesTone" x1="0" y1="0" x2="1" y2="1">
        <stop offset="0" stop-color="#7cc6e6"/>
        <stop offset="0.35" stop-color="#e9d23a"/>
        <stop offset="0.65" stop-color="#d8352e"/>
        <stop offset="1" stop-color="#5fb0dc"/>
      </linearGradient>
      <linearGradient id="tapeTone" x1="0" y1="0" x2="1" y2="1">
        <stop offset="0" stop-color="#b07a52"/>
        <stop offset="0.5" stop-color="#1c1f26"/>
        <stop offset="1" stop-color="#8a5a3a"/>
      </linearGradient>
    </defs>
    <polygon class="band-white" points="0,515 848,293 848,763 0,990" fill="var(--band)"/>
    <g clip-path="url(#photoStrip)">
      <rect x="0" y="280" width="282" height="700" fill="url(#negativesTone)" role="img" aria-label="Photo of rolled 35mm film negatives"/>
      <rect x="289" y="280" width="292" height="700" fill="url(#slidesTone)" role="img" aria-label="Photo of a pile of colourful plastic slide mounts"/>
      <rect x="583" y="280" width="265" height="700" fill="url(#tapeTone)" role="img" aria-label="Photo of a VHS tape on a wooden table"/>
    </g>
  </svg>

  <header class="brand">
    <span class="brand-dot"></span>
    <span class="brand-name">LANTERNLOFT<br>MEDIA</span>
  </header>

  <h1 style="margin:0;font-weight:400">
    <span class="headline-line line-scan">We <span class="big">scan</span> negatives,</span>
    <span class="headline-line line-media">slides and VHS tapes to</span>
    <span class="headline-line line-digital"><span class="big">digital</span> files</span>
  </h1>

  <div class="usb-stick usb-left" role="img" aria-label="Product photo of a branded swivel USB stick"></div>
  <div class="usb-stick usb-right" role="img" aria-label="Product photo of a branded swivel USB stick"></div>

  <p class="benefit benefit-view" style="margin:0">View easily</p>
  <p class="benefit benefit-store" style="margin:0"><span class="lead">Store</span> safely</p>
  <p class="benefit benefit-share" style="margin:0">Share with family</p>
  <p class="benefit benefit-print" style="margin:0"><span class="lead">Print</span> copies</p>

  <footer class="contact">
    <svg class="contact-frame" width="475" height="74" viewBox="0 0 475 74" fill="none" stroke="#ffffff" stroke-width="1.5">
      <polyline points="26,1 1,1 1,73 26,73"/>
      <polyline points="449,1 474,1 474,73 449,73"/>
    </svg>
    <div class="contact-row contact-phone">
      <svg class="contact-icon" viewBox="0 0 24 24">
        <circle cx="12" cy="12" r="11.5" fill="#ffffff"/>
        <path d="M9.5 6.5 L11.5 6.5 L12 9.5 L10.5 10.5 C11 12.5 12 13.7 13.5 14.5 L14.5 13 L17.5 13.5 L17.5 15.5 C17.5 16.5 16.5 17.5 15 17.3 C10.5 16.5 7.5 13 7 9 C6.9 7.6 8 6.5 9.5 6.5 Z" fill="#3a82c2"/>
      </svg>
      <span>Miriam 0482 917 356</span>
    </div>
    <div class="contact-row contact-web">
      <svg class="contact-icon" viewBox="0 0 24 24" fill="none" stroke="#ffffff" stroke-width="1.6">
        <circle cx="12" cy="12" r="10.5"/>
        <ellipse cx="12" cy="12" rx="4.5" ry="10.5"/>
        <line x1="1.5" y1="12" x2="22.5" y2="12"/>
        <path d="M3.5 6.5 H20.5 M3.5 17.5 H20.5"/>
      </svg>
      <span>www.lanternloft.com</span>
    </div>
  </footer>

</main>
</body>
</html>
```